Business Card Design

Tumble Bay is a Laundromat Store
we provide wash and Fold service to Customers who are busy with their life and can not come to the store and do laundry
we have customers who drop their laundry at the store
but now i want to provide service to customers who are not able to come to the store to drop. i will go to their address and pickup the laundry and get it washed folded and delivered
Updates
Can you use the colour in you design which i uploaded and also fusha fluorescent green bright pink
Target Market(s)
all works of life who don't have time to do laundry
Industry/Entity Type
Store
Contact Information for Business Card
TumbleBay Laundromat
482 Orchard Lane
Lynn MA 01957
Look and feel
Each slider illustrates characteristics of the customer's brand and the style your logo design should communicate.

```html
<!DOCTYPE html>
<html lang="en">
<head>
<meta charset="utf-8">
<title>Tumble Bay Laundromat – Business Card</title>
<link href="https://fonts.googleapis.com/css2?family=Roboto+Slab:wght@400;700&family=Roboto:wght@300;400;700&family=Raleway:wght@400&display=swap" rel="stylesheet">
<style>
  :root {
    --backdrop: #1f2022;
    --card-teal: #80c6c7;
    --band-teal: #6aa8a7;
    --ink: #262626;
    --red: #d0161e;
    --white: #ffffff;
    --address-grey: #3f4a4a;
    --rule: rgba(255,255,255,0.6);
  }
  * { margin: 0; padding: 0; box-sizing: border-box; }
  html, body {
    width: 1200px; height: 1000px; overflow: hidden;
    background: var(--backdrop);
  }
  .card {
    position: absolute; left: 100px; top: 220px;
    width: 1000px; height: 560px;
    background: var(--card-teal);
    overflow: hidden;
  }
  .brand {
    position: absolute; left: 40px; top: 30px; width: 400px;
    text-align: center;
  }
  .brand-photo { display: block; margin: 0 auto; }
  .brand-name {
    margin-top: 10px;
    font-family: "Roboto Slab", serif; font-weight: 700;
    font-size: 40px; color: var(--red); letter-spacing: 1px;
  }
  .pitch {
    position: absolute; left: 440px; top: 28px; width: 540px;
    text-align: center; color: var(--ink);
  }
  .headline-top {
    font-family: "Roboto Slab", serif; font-weight: 700;
    font-size: 62px; line-height: 1; letter-spacing: 4px;
  }
  .headline-sub {
    font-family: "Roboto", sans-serif; font-weight: 400;
    font-size: 38px; line-height: 1.15; letter-spacing: 1px;
  }
  .offer {
    margin-top: 18px;
    font-family: "Roboto", sans-serif; font-weight: 400;
    font-size: 48px; line-height: 1.05;
  }
  .offer strong { font-weight: 700; }
  .offer-you {
    font-family: "Roboto", sans-serif; font-weight: 400;
    font-size: 50px; line-height: 1.1; color: var(--red); letter-spacing: 3px;
  }
  .offer-you strong { font-family: "Roboto Slab", serif; font-weight: 700; }
  .details {
    margin-top: 14px;
    font-family: "Roboto Slab", serif; font-size: 25px; line-height: 1.4;
  }
  .details strong { font-weight: 700; }
  .contact-band {
    position: absolute; left: 0; top: 398px; width: 100%; height: 162px;
    background: var(--band-teal);
    padding: 22px 40px 0 38px;
  }
  .call-row { display: flex; align-items: baseline; gap: 34px; }
  .phone {
    font-family: "Roboto Slab", serif; font-weight: 700;
    font-size: 46px; color: var(--red); letter-spacing: 2px;
  }
  .call-line {
    font-family: "Roboto Slab", serif; font-size: 28px; color: var(--white);
  }
  .call-line strong { font-weight: 700; }
  .rule {
    margin-top: 12px; border-top: 2px dotted var(--rule);
  }
  .address {
    margin-top: 10px;
    font-family: "Raleway", sans-serif; font-size: 30px; color: var(--address-grey);
  }
</style>
</head>
<body>
  <main class="card">
    <div class="brand">
      <svg class="brand-photo" width="300" height="300" viewBox="0 0 300 300" role="img" aria-label="Photo of a pink polka-dot sock inside a stainless steel washing machine drum">
        <defs>
          <radialGradient id="drumTone" cx="45%" cy="40%" r="65%">
            <stop offset="0%" stop-color="#e6e8ea"/>
            <stop offset="60%" stop-color="#a9adb1"/>
            <stop offset="100%" stop-color="#d86a8e"/>
          </radialGradient>
        </defs>
        <circle cx="150" cy="150" r="146" fill="url(#drumTone)" stroke="#ffffff" stroke-width="8"/>
      </svg>
      <div class="brand-name">Tumble Bay</div>
    </div>

    <section class="pitch">
      <div class="headline-top">NO TIME</div>
      <div class="headline-sub">FOR WASHING?</div>
      <div class="offer">WE NOW <strong>PICK UP</strong></div>
      <div class="offer-you">FROM <strong>YOU!</strong></div>
      <p class="details">We will pick up, wash, fold and<br>return your clean laundry to <strong>you</strong>.</p>
    </section>

    <footer class="contact-band">
      <div class="call-row">
        <span class="phone">781-555-0148</span>
        <span class="call-line"><strong>Call us now</strong> to lighten your load!</span>
      </div>
      <div class="rule"></div>
      <div class="address">TumbleBay Laundromat • 482 Orchard Lane • Lynn • MA 01957</div>
    </footer>
  </main>
</body>
</html>
```